Harborlight Willow Home Care Business Cards

We are looking to create double sided, sleek business cards for our new Home Health Care Agency, Harborlight Willow Home Care, located in NJ. We want to appear established, professional and at the same time, stand out with a creative and original flair. It should have a luxurious, exclusive feel to it.
The theme colors from our logo should be incorporated into the project.

Our Logo is attached.

Information to be included on the business cards:

Insert Phone Icon: (555)-204-7390
Insert Website Icon: hwhcpx.example
Insert E-mail Icon: info@hwhcpx.example

Follow us on Social Media!
Insert Facebook Icon: (I will provide the link at a later time)
Insert Instagram Icon (I will provide the link at a later time)

In regard to location, we service the areas of: Bayville
Fernhollow
Larch
Vale
Ashford
Heron Heights
Dunmore
Pinecrest
Elmbrook
Briarwood Township
Cedar Landing Beach
Stillwater
Kestrel Bay
Mill Creek

All all it's neighboring areas.

However, that can take up a lot of room...therefore, I had in mind to use the backside of the card to have a MAP with all these areas marked on there...in addition to listing these service locations below the map.

We want the card to appear lively and vibrant.

Please note: I will provide the potential winner with the contact's name later on in the process.

A sample idea is attached below as well.

Use your creative juices!

Good luck!

• A map of our service areas on the back of the double sided card.
Sleek design
Our logo (refer to attachment below)

```html
<!DOCTYPE html>
<html lang="en">
<head>
<meta charset="utf-8">
<title>Harborlight Willow Home Care – Business Cards</title>
<link href="https://fonts.googleapis.com/css2?family=Montserrat:wght@400;500;700&display=swap" rel="stylesheet">
<style>
  :root {
    --page-bg: #dcdcdc;
    --card-white: #ffffff;
    --brand-blue: #0b4d94;
    --brand-blue-deep: #0a4f93;
    --brand-green: #8cc63f;
    --text-grey: #4a4a4a;
    --faint-logo: #3f74b8;
  }
  * { margin: 0; padding: 0; box-sizing: border-box; }
  html, body {
    width: 1200px; height: 1200px; overflow: hidden;
    background: var(--page-bg);
    font-family: "Montserrat", sans-serif;
  }
  .card {
    position: absolute; left: 207px; width: 785px; height: 448px;
    border-radius: 20px; overflow: hidden;
  }
  .card--front { top: 112px; background: var(--card-white); }
  .card--back { top: 640px; background: var(--brand-blue-deep); }

  .corner { position: absolute; }
  .corner--green { top: 0; right: 0; width: 124px; height: 91px; }
  .corner--blue { bottom: 0; left: 0; width: 127px; height: 94px; }

  .brand {
    position: absolute; left: 58px; width: 330px; text-align: center;
    font-weight: 700; text-transform: uppercase; line-height: 1.1;
    white-space: nowrap;
  }
  .brand--front { top: 262px; color: var(--brand-blue); }
  .brand--back { top: 272px; color: var(--faint-logo); }
  .brand__name { font-size: 25px; letter-spacing: 0.3px; }
  .brand__sub { font-size: 15px; letter-spacing: 8px; margin-top: 6px; }

  .divider {
    position: absolute; left: 418px; top: 122px; width: 2px; height: 204px;
    background: var(--brand-green);
  }

  .contact { position: absolute; left: 459px; top: 118px; }
  .contact__name {
    font-size: 29px; font-weight: 700; color: var(--brand-blue);
    letter-spacing: 1px; line-height: 1;
  }
  .contact__role { font-size: 18px; color: var(--text-grey); margin-top: 6px; }
  .contact__list { list-style: none; margin-top: 14px; }
  .contact__item {
    display: flex; align-items: center; gap: 8px;
    font-size: 20px; color: var(--text-grey); height: 25px; white-space: nowrap;
  }
  .contact__item--gap { margin-top: 14px; }
  .contact__icon { width: 15px; height: 15px; flex: none; }

  .areas { position: absolute; left: 456px; top: 38px; list-style: none; }
  .areas__item {
    display: flex; align-items: center; gap: 14px;
    font-size: 22px; color: var(--card-white); height: 28.7px; letter-spacing: 0.3px;
    white-space: nowrap;
  }
  .areas__dot {
    width: 15px; height: 15px; border-radius: 50%;
    background: var(--brand-green); flex: none;
  }
</style>
</head>
<body>

<section class="card card--front">
  <svg class="corner corner--green" viewBox="0 0 124 91"><polygon points="0,0 124,0 124,91" fill="var(--brand-green)"/></svg>
  <svg class="corner corner--blue" viewBox="0 0 127 94"><polygon points="0,0 127,94 0,94" fill="var(--brand-blue)"/></svg>

  <div class="brand brand--front">
    <div class="brand__name">Harborlight Willow</div>
    <div class="brand__sub">Home Care</div>
  </div>

  <div class="divider"></div>

  <div class="contact">
    <h1 class="contact__name">DANIEL MORROW</h1>
    <p class="contact__role">Director</p>
    <ul class="contact__list">
      <li class="contact__item">
        <svg class="contact__icon" viewBox="0 0 16 16"><circle cx="8" cy="8" r="6.5" fill="none" stroke="var(--brand-green)" stroke-width="1.8"/></svg>
        @Icon: hwhcpx.example
      </li>
      <li class="contact__item">
        <svg class="contact__icon" viewBox="0 0 16 16"><circle cx="8" cy="8" r="7" fill="var(--brand-green)"/></svg>
        /Icon: hwhcpx.example
      </li>
      <li class="contact__item contact__item--gap">
        <svg class="contact__icon" viewBox="0 0 16 16"><path d="M4 1.5 L6 1.5 L7 5 L5.5 6.3 Q7 10 10 11 L11.3 9.5 L14.5 10.5 L14.5 12.5 Q13 15 10 14 Q3 11 1.8 4 Q2 2 4 1.5 Z" fill="var(--brand-green)"/></svg>
        (555)-204-7390
      </li>
      <li class="contact__item">
        <svg class="contact__icon" viewBox="0 0 16 16"><rect x="1" y="3" width="14" height="10" fill="none" stroke="var(--brand-green)" stroke-width="1.5"/><polyline points="1,3 8,9 15,3" fill="none" stroke="var(--brand-green)" stroke-width="1.5"/></svg>
        Icon: info@hwhcpx.example
      </li>
      <li class="contact__item">
        <svg class="contact__icon" viewBox="0 0 16 16"><g fill="none" stroke="var(--brand-green)" stroke-width="1.2"><circle cx="8" cy="8" r="6.5"/><ellipse cx="8" cy="8" rx="3" ry="6.5"/><line x1="1.5" y1="8" x2="14.5" y2="8"/><line x1="2.5" y1="4.5" x2="13.5" y2="4.5"/><line x1="2.5" y1="11.5" x2="13.5" y2="11.5"/></g></svg>
        www.Icon: hwhcpx.example
      </li>
    </ul>
  </div>
</section>

<section class="card card--back">
  <div class="brand brand--back">
    <div class="brand__name">Harborlight Willow</div>
    <div class="brand__sub">Home Care</div>
  </div>

  <ul class="areas">
    <li class="areas__item"><span class="areas__dot"></span>Fernhollow</li>
    <li class="areas__item"><span class="areas__dot"></span>Larch</li>
    <li class="areas__item"><span class="areas__dot"></span>Vale</li>
    <li class="areas__item"><span class="areas__dot"></span>Ashford</li>
    <li class="areas__item"><span class="areas__dot"></span>Heron Heights</li>
    <li class="areas__item"><span class="areas__dot"></span>Dunmore</li>
    <li class="areas__item"><span class="areas__dot"></span>Pinecrest</li>
    <li class="areas__item"><span class="areas__dot"></span>Elmbrook</li>
    <li class="areas__item"><span class="areas__dot"></span>Briarwood Township</li>
    <li class="areas__item"><span class="areas__dot"></span>Cedar Landing Beach</li>
    <li class="areas__item"><span class="areas__dot"></span>Stillwater</li>
    <li class="areas__item"><span class="areas__dot"></span>Kestrel Bay</li>
    <li class="areas__item"><span class="areas__dot"></span>Mill Creek</li>
  </ul>
</section>

</body>
</html>
```